Business Card Design/Stationary Design

We would like designers to submit cool, hip business card designs (plus stationary designs) for a new, upstart software development company located in Toronto.
If you have any questions, please email us.
For inspiration on designs:
http://cardmuse.example/cool-business-cards/
http://layoutnotes.example/2008/05/36-cool-business-cards-you-should%E2%80%99ve-seen.html
http://gigharbor.example/general/18-smokin-hot-business-card-designs/

Card info:

Selvakumar (Selv) Nadarasan

Founder and CEO

47 Brindle Court, Suite 311

Toronto, ON M4K 2T8

Phone: 647-512-7730

Mobile: 416-273-5094

Fax: 647-512-7731

Email: selvakumar.nadarasan@mailbrook.example

www.quendrix.example
Updates

Hi everyone,

In terms of all the designs I have seen so far, here is what I like:

1.  I really like the "back" part of this design.  The "front" looks pretty decent as well, but for the "front", look at #2 on this list.  I like that.

http://www.pitchboard.example/image.aspx?imageLocation=1000_10001_2000_image.jpg&type=design300px&whiteLabelCustId=9999

2. "Side 1" of this I like, the front needs to be reworked.

http://www.pitchboard.example/image.aspx?imageLocation=1000_10002_2000_image.png&type=design300px&whiteLabelCustId=9999

3. http://www.pitchboard.example/image.aspx?imageLocation=1000_10003_2000_image.jpg&type=design300px&whiteLabelCustId=9999

4. http://www.pitchboard.example/image.aspx?imageLocation=1000_10004_2000_image.jpg&type=design300px&whiteLabelCustId=9999

Target Market(s)

We are focused on enterprise customers right now, so businesses with a long-term goal of also reaching out to the consumer market as well.

Industry/Entity Type

Software

Requirements
Must have
• Must look cool, ultra-modern, clean and eye-catching. Must incorporate our logo and the colors found in the logo.

```html
<!DOCTYPE html>
<html lang="en">
<head>
<meta charset="utf-8">
<title>Quendrix Technologies Inc. — Stationery Set</title>
<link rel="stylesheet" href="https://fonts.googleapis.com/css2?family=Open+Sans:wght@400;600&display=swap">
<style>
  :root {
    --ink: #0b0b0b;
    --paper: #ffffff;
    --lime: #8fd11f;
    --lime-pale: #eef7c8;
    --grey-text: #5a5a5a;
    --card-text: #d9d9d9;
    --flap-line: #3a3a3a;
  }
  * { box-sizing: border-box; margin: 0; padding: 0; }
  html, body {
    width: 1200px; height: 922px; overflow: hidden;
    background: var(--paper);
    font-family: "Open Sans", Arial, sans-serif;
  }
  .canvas { position: relative; width: 1200px; height: 922px; }
  .piece {
    position: absolute; overflow: hidden;
    box-shadow: 0 2px 8px rgba(0,0,0,0.28);
  }
  .piece svg.shape { position: absolute; inset: 0; }

  /* brand lockup: dot + name, set on the diagonal */
  .brand {
    position: absolute; display: flex; align-items: center;
    transform: translate(-50%, -50%) rotate(-45deg);
    white-space: nowrap;
  }
  .brand-dot { flex: none; border-radius: 50%; background: var(--lime); }
  .brand-text { display: flex; flex-direction: column; align-items: flex-start; }
  .brand-name { font-weight: 600; color: var(--ink); line-height: 1; letter-spacing: 0.5px; }
  .brand-sub { font-weight: 600; color: var(--ink); line-height: 1; letter-spacing: 0.6px; margin-top: 2px; }

  /* letterhead */
  .letterhead { left: 38px; top: 38px; width: 612px; height: 792px; background: var(--paper); }
  .letterhead .brand { left: 128px; top: 68px; gap: 6px; }
  .letterhead .brand-dot { width: 24px; height: 24px; }
  .letterhead .brand-name { font-size: 24px; }
  .letterhead .brand-sub { font-size: 5.5px; margin-left: 16px; }
  .letterhead-contact {
    position: absolute; left: 598px; top: 24px;
    transform-origin: 0 0; transform: rotate(90deg);
    display: flex; align-items: flex-start;
    font-size: 8.5px; color: var(--grey-text); line-height: 11px; white-space: nowrap;
  }
  .letterhead-contact .block { width: 76px; }
  .letterhead-contact .block.address { width: 114px; }
  .letterhead-contact .rule { width: 16px; height: 1.5px; background: var(--lime); margin: 5px 11px 0 0; }

  /* business cards */
  .card-front { left: 698px; top: 67px; width: 252px; height: 143px; background: var(--ink); }
  .card-back  { left: 698px; top: 230px; width: 252px; height: 143px; background: var(--ink); }
  .center-mark {
    position: absolute; left: 0; right: 0; display: flex; align-items: center; justify-content: center; gap: 5px;
  }
  .center-mark .dot { border-radius: 50%; background: var(--lime); }
  .center-mark .word { color: var(--lime); font-weight: 600; line-height: 1; }
  .card-front .center-mark { top: 56px; }
  .card-front .center-mark .dot { width: 12px; height: 12px; }
  .card-front .center-mark .word { font-size: 15px; }
  .site {
    position: absolute; left: 0; right: 0; text-align: center;
    color: var(--lime); font-size: 6px; letter-spacing: 0.2px;
  }
  .card-front .site { top: 100px; }

  .card-details { position: absolute; left: 10px; top: 11px; color: var(--card-text); white-space: nowrap; }
  .card-details .person { color: var(--lime); font-size: 9px; line-height: 12px; }
  .card-details .role { font-size: 4.6px; line-height: 7px; margin-top: 2px; }
  .card-details .primary { font-size: 6.6px; line-height: 12px; margin-top: 1px; }
  .card-details .secondary { font-size: 4.8px; line-height: 12px; margin-top: 23px; }
  .card-details .label { color: var(--lime); }
  .card-back .brand { left: 206px; top: 100px; gap: 4px; }
  .card-back .brand-dot { width: 13px; height: 13px; }
  .card-back .brand-name { font-size: 15px; }
  .card-back .brand-sub { font-size: 3.6px; margin-left: 10px; }

  /* envelopes */
  .envelope-front { left: 698px; top: 394px; width: 386px; height: 210px; background: var(--ink); }
  .envelope-front .center-mark { top: 84px; }
  .envelope-front .center-mark .dot { width: 16px; height: 16px; }
  .envelope-front .center-mark .word { font-size: 21px; }
  .envelope-front .site { top: 140px; font-size: 7px; }

  .envelope-back { left: 698px; top: 620px; width: 386px; height: 210px; background: var(--ink); }
  .envelope-back .brand { left: 336px; top: 156px; gap: 5px; }
  .envelope-back .brand-dot { width: 16px; height: 16px; }
  .envelope-back .brand-name { font-size: 18px; }
  .envelope-back .brand-sub { font-size: 4.2px; margin-left: 12px; }
</style>
</head>
<body>
<main class="canvas">

  <!-- Letterhead -->
  <section class="piece letterhead" aria-label="Letterhead">
    <svg class="shape" width="612" height="792" viewBox="0 0 612 792" aria-hidden="true">
      <circle cx="410" cy="650" r="180" fill="none" stroke="var(--lime-pale)" stroke-width="60"/>
      <polygon points="0,0 112,0 0,112" fill="var(--ink)"/>
      <polygon points="112,0 124,0 0,124 0,112" fill="var(--lime)"/>
    </svg>
    <div class="brand">
      <span class="brand-dot"></span>
      <div class="brand-text">
        <span class="brand-name">Quendrix</span>
        <span class="brand-sub">TECHNOLOGIES INC.</span>
      </div>
    </div>

    <div class="letterhead-contact">
      <div class="block">T: 647-512-7730<br>F: 647-512-7731</div>
      <div class="rule"></div>
      <div class="block address">47 Brindle Court, Suite 311<br>Toronto, ON M4K 2T8</div>
      <div class="rule"></div>
      <div class="block">www.quendrix.example</div>
    </div>
  </section>

  <!-- Business card, front -->
  <section class="piece card-front" aria-label="Business card front">
    <div class="center-mark"><span class="dot"></span><span class="word">Quendrix</span></div>
    <p class="site">www.quendrix.example</p>
  </section>

  <!-- Business card, back -->
  <section class="piece card-back" aria-label="Business card back">
    <svg class="shape" width="252" height="143" viewBox="0 0 252 143">
      <polygon points="250,0 252,0 252,143 110,143" fill="var(--paper)"/>
      <polygon points="238,0 250,0 110,143 97,143" fill="var(--lime)"/>
    </svg>
    <div class="card-details">
      <p class="person">Selvakumar (Selv) Nadarasan</p>
      <p class="role">Founder and CEO</p>
      <p class="primary"><span class="label">Email:</span> selvakumar.nadarasan@mailbrook.example<br><span class="label">Mobile:</span> 416 273 5094</p>
      <p class="secondary"><span class="label">Tel:</span> 647-512-7730<br><span class="label">Fax:</span> 647-512-7731<br>47 Brindle Court, Suite 311<br>Toronto, ON M4K 2T8</p>
    </div>
    <div class="brand">
      <span class="brand-dot"></span>
      <div class="brand-text">
        <span class="brand-name">Quendrix</span>
        <span class="brand-sub">TECHNOLOGIES INC.</span>
      </div>
    </div>
  </section>

  <!-- Envelope, front -->
  <section class="piece envelope-front" aria-label="Envelope front">
    <div class="center-mark"><span class="dot"></span><span class="word">Quendrix</span></div>
    <p class="site">www.quendrix.example</p>
  </section>

  <!-- Envelope, back -->
  <section class="piece envelope-back" aria-label="Envelope back">
    <svg class="shape" width="386" height="210" viewBox="0 0 386 210">
      <polyline points="0,13 199,74 386,13" fill="none" stroke="var(--flap-line)" stroke-width="1"/>
      <polygon points="386,51 386,210 227,210" fill="var(--paper)"/>
      <polygon points="386,35 386,51 227,210 210,210" fill="var(--lime)"/>
    </svg>
    <div class="brand">
      <span class="brand-dot"></span>
      <div class="brand-text">
        <span class="brand-name">Quendrix</span>
        <span class="brand-sub">TECHNOLOGIES INC.</span>
      </div>
    </div>
  </section>

</main>
</body>
</html>
```